Staffing Firm - Business Cards and Stationary
Business Cards, Letterhead, Envelopes and Brochure Layout
I need double sided standard sized Business Card [3.5" x 2"]
Use whatever fonts that you think are best.
Professional
Todd Dunlap
President/CEO
2250 North Birch Avenue, Ste 730
Houston, TX 77027
Direct Line - 832-555-0143
tdunlap@kelvor.com
www.kelvor.com
We would like them to be memorable but professional.
Possibly put the various divisions?
We will need layouts for each group/division.

```html
<!DOCTYPE html>
<html lang="en">
<head>
<meta charset="utf-8">
<title>Kelvor Staffing – Business Cards</title>
<link rel="stylesheet" href="https://fonts.googleapis.com/css2?family=Cinzel:wght@400;600&family=Cormorant+Garamond:wght@500&family=Lato:wght@400&display=swap">
<style>
  :root {
    --backdrop: #2a2522;
    --card-white: #ffffff;
    --card-black-top: #2b2b2b;
    --card-black-bottom: #060606;
    --ink: #1d1d1d;
    --ink-soft: #555555;
    --back-text: #e8e8e8;
    --back-list: #9a9a9a;
    --accent-staffing: #6d6d6d;
    --accent-credit: #4f7a3a;
    --accent-search: #8a2a8c;
    --accent-services: #b3222a;
    --accent-tech: #2c4f9a;
  }
  * { margin: 0; padding: 0; box-sizing: border-box; }
  html, body { width: 1200px; height: 874px; overflow: hidden; }
  body { background: var(--backdrop); }

  .card-sheet {
    position: absolute;
    left: 360px;
    top: 34px;
    display: grid;
    grid-template-columns: 270px 270px;
    grid-auto-rows: 150px;
    row-gap: 13px;
  }

  .card { position: relative; overflow: hidden; }

  .card-front { background: var(--card-white); color: var(--ink); }
  .card-back {
    background: linear-gradient(160deg, var(--card-black-top), var(--card-black-bottom) 70%);
    color: var(--back-text);
  }

  .logo-name {
    font-family: "Cinzel", serif;
    font-weight: 400;
    letter-spacing: 0.06em;
    line-height: 1;
  }
  .card-front .logo-name {
    position: absolute; left: 34px; top: 16px;
    font-size: 17px; color: var(--ink);
  }
  .division-tag {
    position: absolute; left: 34px; top: 54px; width: 118px;
    text-align: right;
    font-family: "Lato", sans-serif; font-size: 6.5px; font-style: italic;
    color: var(--accent);
  }

  .holder { position: absolute; left: 26px; top: 88px; }
  .holder-name {
    font-family: "Cormorant Garamond", serif; font-weight: 500;
    font-size: 17px; color: var(--ink);
  }
  .holder-title {
    font-family: "Cormorant Garamond", serif; font-size: 10px;
    color: var(--ink-soft); margin-left: 14px;
  }

  .contact {
    position: absolute; left: 140px; top: 80px;
    padding-left: 6px; border-left: 1px solid var(--accent);
    font-family: "Lato", sans-serif; font-size: 5.5px; line-height: 1.55;
    color: var(--ink-soft);
  }

  .card-back .logo-name {
    position: absolute; left: 44px; top: 30px;
    font-size: 18px; color: var(--back-text);
  }
  .division-list {
    position: absolute; left: 90px; top: 78px; list-style: none;
    font-family: "Lato", sans-serif; font-size: 6px; line-height: 1.5;
    letter-spacing: 0.05em; color: var(--back-list);
  }

  .div-staffing { --accent: var(--accent-staffing); }
  .div-credit { --accent: var(--accent-credit); }
  .div-search { --accent: var(--accent-search); }
  .div-services { --accent: var(--accent-services); }
  .div-tech { --accent: var(--accent-tech); }
</style>
</head>
<body>
<main class="card-sheet">

  <!-- Staffing solutions -->
  <section class="card card-front div-staffing">
    <div class="logo-name">KELVOR<br>STAFFING</div>
    <div class="division-tag">staffing solutions</div>
    <div class="holder"><div class="holder-name">Todd Dunlap</div><div class="holder-title">President/CEO</div></div>
    <address class="contact">2250 North Birch Avenue, Ste 730<br>Houston, TX 77027<br>Direct Line - 832-555-0143<br>tdunlap@kelvor.com<br>www.kelvor.com</address>
  </section>
  <section class="card card-back">
    <div class="logo-name">KELVOR<br>STAFFING</div>
    <ul class="division-list"><li>staffing solutions</li><li>credit and risk group</li><li>professional search group</li><li>staffing services group</li><li>technology services group</li></ul>
  </section>

  <!-- Credit and risk group -->
  <section class="card card-front div-credit">
    <div class="logo-name">KELVOR<br>STAFFING</div>
    <div class="division-tag">credit and risk group</div>
    <div class="holder"><div class="holder-name">Todd Dunlap</div><div class="holder-title">President/CEO</div></div>
    <address class="contact">2250 North Birch Avenue, Ste 730<br>Houston, TX 77027<br>Direct Line - 832-555-0143<br>tdunlap@kelvor.com<br>www.kelvor.com</address>
  </section>
  <section class="card card-back">
    <div class="logo-name">KELVOR<br>STAFFING</div>
    <ul class="division-list"><li>staffing solutions</li><li>credit and risk group</li><li>professional search group</li><li>staffing services group</li><li>technology services group</li></ul>
  </section>

  <!-- Professional search group -->
  <section class="card card-front div-search">
    <div class="logo-name">KELVOR<br>STAFFING</div>
    <div class="division-tag">professional search group</div>
    <div class="holder"><div class="holder-name">Todd Dunlap</div><div class="holder-title">President/CEO</div></div>
    <address class="contact">2250 North Birch Avenue, Ste 730<br>Houston, TX 77027<br>Direct Line - 832-555-0143<br>tdunlap@kelvor.com<br>www.kelvor.com</address>
  </section>
  <section class="card card-back">
    <div class="logo-name">KELVOR<br>STAFFING</div>
    <ul class="division-list"><li>staffing solutions</li><li>credit and risk group</li><li>professional search group</li><li>staffing services group</li><li>technology services group</li></ul>
  </section>

  <!-- Staffing services group -->
  <section class="card card-front div-services">
    <div class="logo-name">KELVOR<br>STAFFING</div>
    <div class="division-tag">staffing services group</div>
    <div class="holder"><div class="holder-name">Todd Dunlap</div><div class="holder-title">President/CEO</div></div>
    <address class="contact">2250 North Birch Avenue, Ste 730<br>Houston, TX 77027<br>Direct Line - 832-555-0143<br>tdunlap@kelvor.com<br>www.kelvor.com</address>
  </section>
  <section class="card card-back">
    <div class="logo-name">KELVOR<br>STAFFING</div>
    <ul class="division-list"><li>staffing solutions</li><li>credit and risk group</li><li>professional search group</li><li>staffing services group</li><li>technology services group</li></ul>
  </section>

  <!-- Technology services group -->
  <section class="card card-front div-tech">
    <div class="logo-name">KELVOR<br>STAFFING</div>
    <div class="division-tag">technology services group</div>
    <div class="holder"><div class="holder-name">Todd Dunlap</div><div class="holder-title">President/CEO</div></div>
    <address class="contact">2250 North Birch Avenue, Ste 730<br>Houston, TX 77027<br>Direct Line - 832-555-0143<br>tdunlap@kelvor.com<br>www.kelvor.com</address>
  </section>
  <section class="card card-back">
    <div class="logo-name">KELVOR<br>STAFFING</div>
    <ul class="division-list"><li>staffing solutions</li><li>credit and risk group</li><li>professional search group</li><li>staffing services group</li><li>technology services group</li></ul>
  </section>

</main>
</body>
</html>
```